Web Design Project

*** This project has been temporarily placed on hold as the Logo Design needs to be completed first. You are all welcome to participate on it as well: http://gigs.pitchboardly.com/brief.aspx?id=482917 This project will be reopened soon***

Revamp current website adding newly designed logo and creating layout that is good on desktops, tablets, and cell phones.

Current website can be viewed at www.vennatistudio.com

Will you see the website is small but graphics heavy in the gallery. The gallery needs to be setup so that it is easy to maintain the links and update the photos.

Needs to have high visual impact.

I need a new logo and website layout designed for my partner's business. This is a birthday present. His business is interior painting, wallpapering and design. He also has access to a wide variety of products including carpet, fabrics, furniture, wallpaper, tile, countertops, etc. I have attached some screen shots of his website for reference. He is a one man shop and has a stellar reputation with his customers. He is on-time, very tidy, excellent with animals, and always finishes on time and on budget. There are no restrictions on colors or fonts. The logo needs to work well with the website, business cards and printed materials. The website needs to flow content for device size so it looks just as good on a cell phone or tablet as it does on a desktop computer. Whatever the heck that's called! Thanks. I am looking forward to seeing everyone's ideas.
Updates

Hi Designers, We've reopened this project as our logo design project has just completed. Please refer to the uploaded files and make use of either Horizontal or Vertical versions of the logo depending on what you think is suitable for your design proposals. We look forward to your creative submissions!

Target Market(s)

Consumers looking for interior design, painting, and wallpapering as well as interior products such as flooring, window treatments, reupholstering, counter tops, etc.

Industry/Entity Type

Cell Phone

Requirements
Must have
• Clean, sharp, visual impact (at least on the home page)
Should not have
• Clutter.

```html
<!DOCTYPE html>
<html lang="en">
<head>
<meta charset="utf-8">
<title>Venatti Interior Designs</title>
<link href="https://fonts.googleapis.com/css2?family=Roboto:wght@400;500;700&family=Bitter:wght@500&display=swap" rel="stylesheet">
<style>
:root{
  --purple:#22103f;
  --purple-deep:#1c0c36;
  --tan:#a99568;
  --tan-light:#b8a679;
  --lavender:#efedf8;
  --grey:#ebebeb;
  --red:#a8171c;
  --ink:#333;
  --white:#fff;
  --placeholder:#d9d6df;
}
*{box-sizing:border-box;margin:0;padding:0}
html,body{width:987px;height:1200px;overflow:hidden;background:var(--white)}
body{position:relative;font-family:'Roboto',sans-serif;color:var(--ink)}
.abs{position:absolute}

/* header */
.brand{left:108px;top:17px;display:flex;align-items:center;gap:10px}
.brand-mark{width:36px;height:36px;background:var(--purple)}
.brand-name{font-size:21px;font-weight:700;color:var(--purple);line-height:1.05;letter-spacing:.3px}
.social-tab{left:697px;top:0;width:180px;height:27px;background:var(--red);border-radius:0 0 20px 20px;display:flex;justify-content:center;align-items:center;gap:26px}
.social-tab span,.social-row span{width:13px;height:13px;border-radius:50%;background:var(--white)}
.header-phone{left:712px;top:38px;display:flex;align-items:center;gap:10px;font-size:19px;color:#222}
.phone-dot{width:24px;height:24px;border-radius:50%;background:#f39a1e;display:flex;align-items:center;justify-content:center}

/* nav */
.nav{left:0;top:76px;width:987px;height:38px;background:var(--tan)}
.nav ul{list-style:none;position:absolute;left:108px;top:0;display:flex;height:38px}
.nav li{color:var(--white);font-size:13px;font-weight:500;line-height:38px;padding:0 21px}
.nav li.active{background:var(--purple)}
.nav-mail{right:110px;top:0;line-height:38px;font-size:11px;color:var(--white);display:flex;align-items:center;gap:8px}

/* hero */
.hero{left:0;top:114px;width:987px;height:297px;background:linear-gradient(100deg,#9c1f4d 0%,#b02a5c 25%,#3a1a22 45%,#6b4a5a 58%,#b8b4bd 75%,#8d4f9a 100%)}
.hero-caption{left:120px;top:370px;font-family:'Bitter',serif;font-size:26px;font-weight:500;color:var(--white);white-space:nowrap}
.hero-dots{left:812px;top:381px;display:flex;gap:6px}
.hero-dots span{width:8px;height:8px;border-radius:50%;background:var(--white)}
.hero-dots span.on{background:#f39a1e}

/* services */
.service{top:436px;height:77px;display:flex;align-items:center;gap:14px;padding-left:12px;color:var(--white);font-size:19px;font-weight:700;background:var(--tan)}
.service.primary{background:var(--purple)}
.service-icon{width:54px;height:54px;border-radius:50%;background:var(--white);display:flex;align-items:center;justify-content:center}

/* about */
.about{left:0;top:541px;width:987px;height:236px;background:var(--lavender)}
.about-kicker{left:108px;top:557px;font-size:21px;color:#222;font-weight:400}
.about-title{left:108px;top:578px;font-size:33px;color:#111;font-weight:400}
.about-title em{font-style:normal;color:var(--tan)}
.about-rule{left:108px;top:626px;width:492px;height:1px;background:#cfcbd9}
.about-copy{left:108px;top:636px;width:492px;font-size:11.4px;line-height:19px;color:#333;text-align:justify}
.read-more{left:533px;top:737px;font-size:12px;font-weight:500;color:var(--tan)}
.review-card{left:625px;top:562px;width:252px;height:191px;background:var(--white);box-shadow:0 4px 10px rgba(0,0,0,.12);text-align:center;padding-top:4px;font-size:12px;color:#222}
.review-card b{font-weight:700}
.badge-placeholder{left:710px;top:610px;width:84px;height:120px;background:var(--placeholder);border-radius:4px}

/* gallery */
.gallery{left:0;top:777px;width:987px;height:198px;background:var(--grey);border-top:3px solid var(--purple)}
.gallery-tab{left:405px;top:777px;width:183px;height:33px;background:var(--purple);color:var(--white);font-size:17px;font-weight:400;text-align:center;line-height:30px;border-radius:0 0 14px 14px}
.thumb{top:834px;width:163px;height:111px}
.thumb-label{position:absolute;left:0;bottom:0;width:100%;height:24px;background:rgba(0,0,0,.35);color:var(--white);font-size:11px;font-weight:700;line-height:24px;padding-left:7px}
.arrow{top:873px;width:38px;height:38px}

/* footer */
.footer{left:0;top:975px;width:987px;height:225px;background:var(--purple-deep)}
.testimonials{left:108px;top:975px;width:231px;height:225px;background:var(--tan)}
.col-title{font-size:18px;color:var(--white)}
.quote-box{left:121px;top:1025px;width:204px;height:120px;background:var(--tan-light);border-radius:6px;padding:9px 10px 0 14px;font-size:11px;line-height:15px;color:var(--white)}
.quote-mark{font-size:18px;font-weight:700;color:var(--purple);line-height:0;vertical-align:-4px}
.testimonial-dots{left:129px;top:1167px;display:flex;gap:4px}
.testimonial-dots span{width:6px;height:6px;border-radius:50%;background:var(--white)}
.testimonial-dots span.off{opacity:.55}
.author{left:210px;top:1163px;font-size:12px;font-weight:700;color:var(--white)}
.email-field{left:378px;top:1022px;width:228px;height:30px;background:var(--white);font-size:11px;color:#888;line-height:30px;padding-left:6px}
.submit{left:606px;top:1022px;width:69px;height:30px;background:var(--red);color:var(--white);font-size:12px;font-weight:700;line-height:30px;text-align:center}
.footer-line{height:1px;background:#3a2a57}
.contact{font-size:11px;color:var(--white);line-height:16px;display:flex;gap:8px;align-items:flex-start}
.social-row{left:727px;top:1030px;display:flex;gap:24px}
.social-row span{width:16px;height:16px}
.footer-brand{left:727px;top:1102px;display:flex;align-items:center;gap:6px;color:var(--white);font-size:13px;font-weight:700;line-height:1.1}
.footer-brand i{width:14px;height:14px;background:var(--white)}
.copyright{left:0;top:1170px;width:987px;text-align:center;font-size:11px;color:#d8d3e3;padding-left:200px}
</style>
</head>
<body>

<header>
  <div class="abs brand">
    <div class="brand-mark"></div>
    <div class="brand-name">VENATTI<br>INTERIOR DESIGNS</div>
  </div>
  <div class="abs social-tab" aria-label="Social links"><span></span><span></span><span></span><span></span></div>
  <div class="abs header-phone">
    <span class="phone-dot"><svg width="12" height="12" viewBox="0 0 24 24"><path fill="#fff" d="M6.6 10.8a15 15 0 0 0 6.6 6.6l2.2-2.2c.3-.3.7-.4 1-.2 1.1.4 2.3.6 3.6.6.6 0 1 .4 1 1V20c0 .6-.4 1-1 1A17 17 0 0 1 3 4c0-.6.4-1 1-1h3.5c.6 0 1 .4 1 1 0 1.3.2 2.5.6 3.6.1.3 0 .7-.2 1z"/></svg></span>
    (555) 214-3380
  </div>
</header>

<nav class="abs nav">
  <ul>
    <li class="active">HOME</li><li>ABOUT US</li><li>PRODUCTS</li><li>SERVICES</li><li>GALLERY</li><li>CONTACT US</li>
  </ul>
  <div class="abs nav-mail">
    <svg width="16" height="12" viewBox="0 0 16 12"><rect x="1" y="1" width="14" height="10" fill="none" stroke="#fff" stroke-width="1.5"/><path d="M1 1l7 6 7-6" fill="none" stroke="#fff" stroke-width="1.5"/></svg>
    support@vennatistudio.com
  </div>
</nav>

<section>
  <div class="abs hero" role="img" aria-label="Photo of a modern living room with a magenta feature wall, wall-mounted TV and purple lounge chairs"></div>
  <h1 class="abs hero-caption">A Wonderful New Look Is Within Anyone's Reach</h1>
  <div class="abs hero-dots"><span></span><span class="on"></span><span></span><span></span></div>
</section>

<section>
  <div class="abs service primary" style="left:108px;width:276px">
    <span class="service-icon"><svg width="30" height="30" viewBox="0 0 24 24"><path fill="#22103f" d="M12 3 2 12h3v8h5v-5h4v5h5v-8h3z"/></svg></span>INTERIOR PAINTING
  </div>
  <div class="abs service" style="left:405px;width:240px">
    <span class="service-icon"><svg width="28" height="28" viewBox="0 0 24 24"><rect x="5" y="4" width="14" height="16" rx="2" fill="#a99568"/></svg></span>WALLPAPER
  </div>
  <div class="abs service" style="left:666px;width:213px">
    <span class="service-icon"><svg width="28" height="28" viewBox="0 0 24 24"><path d="M5 19 19 5" stroke="#a99568" stroke-width="4"/><path d="M5 5l14 14" stroke="#a99568" stroke-width="2"/></svg></span>DESIGN
  </div>
</section>

<section>
  <div class="abs about"></div>
  <h2 class="abs about-kicker">About</h2>
  <h2 class="abs about-title">Venatti <em>Interior Designs</em></h2>
  <div class="abs about-rule"></div>
  <p class="abs about-copy">Lorem ipsum dolor sit amet, consecte tuer adipise my nibh euidsgfhdfvds fmdiod tindcidu nt utre magmi aliquam erat volutpat. Ut wisi enim ad minim veniam quiifcs nost rutatxsion ulasdfilaei pit lobortisi nisl ut aliquip ex ea commodo conse fqfihjuis autem veli efghfgum idolor in hensgdrer vulate velitm eonsequatvel illum dol deorsffje feugiat nulla facilisis adt vero eros et accsiusao odiol digisml qui bldcjhdja praesent luptatum zzril delonrit.</p>
  <div class="abs read-more">READ MORE</div>
  <div class="abs review-card">Read Unbiased Consumer Reviews Online<br>at <b>ReviewHub.com</b></div>
  <div class="abs badge-placeholder" role="img" aria-label="Review service award badge"></div>
</section>

<section>
  <div class="abs gallery"></div>
  <h2 class="abs gallery-tab">Our Work Gallery</h2>
  <svg class="abs arrow" style="left:63px" viewBox="0 0 38 38"><circle cx="19" cy="19" r="17" fill="none" stroke="#8a8a8a" stroke-width="3"/><path d="M22 11l-8 8 8 8" fill="none" stroke="#8a8a8a" stroke-width="3"/></svg>
  <div class="abs thumb" style="left:114px;background:linear-gradient(135deg,#5a4a44,#d8d2cc 60%,#b01e22)" role="img" aria-label="Photo of a living room with white sofa and red accents"><span class="thumb-label">LOREM ISPUM</span></div>
  <div class="abs thumb" style="left:310px;background:linear-gradient(135deg,#6a6a6e,#b9b3aa 55%,#9b2a22)" role="img" aria-label="Photo of a grey media wall with red shelving"><span class="thumb-label">LOREM ISPUM</span></div>
  <div class="abs thumb" style="left:508px;background:linear-gradient(135deg,#cfc7b8,#a79a86 55%,#e6e0d6)" role="img" aria-label="Photo of a bright beige lounge with large windows"><span class="thumb-label">LOREM ISPUM</span></div>
  <div class="abs thumb" style="left:711px;background:linear-gradient(135deg,#4d5a3a,#d9d6cf 50%,#2d2a28)" role="img" aria-label="Photo of a modern room with green wall art and dark sofa"><span class="thumb-label">LOREM ISPUM</span></div>
  <svg class="abs arrow" style="left:882px" viewBox="0 0 38 38"><circle cx="19" cy="19" r="17" fill="none" stroke="#8a8a8a" stroke-width="3"/><path d="M16 11l8 8-8 8" fill="none" stroke="#8a8a8a" stroke-width="3"/></svg>
</section>

<footer>
  <div class="abs footer"></div>
  <div class="abs testimonials"></div>
  <div class="abs col-title" style="left:124px;top:986px;display:flex;gap:9px;align-items:center">
    <svg width="20" height="18" viewBox="0 0 20 18"><rect x="0" y="0" width="14" height="10" rx="2" fill="#fff"/><rect x="6" y="5" width="14" height="10" rx="2" fill="#fff" opacity=".8"/></svg>Client Testimonials
  </div>
  <div class="abs quote-box"><span class="quote-mark">&ldquo;</span> Lorem ipsum dolor conseetueri adipiscing esed diam nonummy nibh euismod tincidunt ut laoreet dolore magna aliquam erat volwisi laoreet dolore magna aliqm erat volut wisi enim ad minim veniam. <span class="quote-mark">&rdquo;</span></div>
  <div class="abs testimonial-dots"><span></span><span></span><span class="off"></span><span class="off"></span></div>
  <div class="abs author">Dana Whitlow</div>

  <div class="abs col-title" style="left:378px;top:988px">News Letter Signup</div>
  <div class="abs email-field">Enter Your Email</div>
  <div class="abs submit">SUBMIT</div>
  <div class="abs footer-line" style="left:378px;top:1073px;width:477px"></div>
  <div class="abs contact" style="left:380px;top:1084px">
    <svg width="10" height="15" viewBox="0 0 10 15"><path d="M5 0a5 5 0 0 1 5 5c0 4-5 10-5 10S0 9 0 5a5 5 0 0 1 5-5z" fill="#fff"/><circle cx="5" cy="5" r="2" fill="#1c0c36"/></svg>
    <span>Street Name City Name<br>State Zipcode</span>
  </div>
  <div class="abs contact" style="left:548px;top:1087px;font-size:15px">
    <svg width="10" height="14" viewBox="0 0 10 14"><rect x="1" y="0" width="8" height="14" rx="1.5" fill="#fff"/></svg>(555) 214-3380
  </div>
  <div class="abs contact" style="left:380px;top:1132px">
    <svg width="13" height="10" viewBox="0 0 13 10"><rect width="13" height="10" fill="#fff"/><path d="M0 0l6.5 5L13 0" fill="none" stroke="#1c0c36"/></svg>support@venattiinteriors.com
  </div>
  <div class="abs footer-line" style="left:378px;top:1158px;width:477px"></div>

  <div class="abs" style="left:708px;top:990px;width:1px;height:68px;background:#3a2a57"></div>
  <div class="abs col-title" style="left:727px;top:988px">Social Connect</div>
  <div class="abs social-row" aria-label="Social links"><span></span><span></span><span></span><span></span></div>
  <div class="abs footer-brand"><i></i>VENATTI<br>INTERIOR DESIGNS</div>

  <p class="abs copyright">&copy; 2014 VenattiInteriors.com . All Rights Reserved.</p>
</footer>

</body>
</html>
```